Velmor PashuのRTZの電子書籍表紙デザインをお願いします。

*週末ごとに和みを探す読者へ贈る癒やしの四季手帳*というタイトルの表紙デザインの発注です。
サブタイトル 猫の昼寝は街を照らす
猫の昼寝は毎日を照らす
私は猫の昼寝に癒された
になります。
お笑い要素の多い1日1笑いみたいな本の表紙です。

初めての表紙デザイン依頼なので、よく勝手がわかっていませんので、
出来上がったデザインを作家グループの中で投票にかけて、
一番投票得票数の多かったものを表紙デザインとして選ばせていただきたいと考えております。
もしかしたら、その中で、何か修正依頼など来るかもしれませんが、
それも含めて、ご対応していただける方よろしくお願いします。

1部内容の抜粋を記載します。

その他何かご不明な点がございましたら、お気軽にご質問下さい。
よろしくお願いいたします。
すいません。作家名は後でお伝えします。作家名もどこかに挿入いただきたいです。よろしくお願いします。
データサイズですが、推奨サイズでJPEGファイルでご納品下さい、よろしくお願いします。
皆様、たくさんのご応募まことにありがとうございました。
現在、作家グループへ全体回覧のメールを致しました。
皆様の投票結果までお待ちください。
また、この度、いろいろな作品に触れさせていただきましたこと本当に
本当に感謝いたします。
今回の表紙に関しましては、どうしても1名しか選べない状況がございますこと
また、選挙による投票にて決定致しますこと、ご理解何卒よろしくお願い申しあげます。
また、もしも、今回当選に至らないことがありましても、
今後も私自身は作家生活を継続予定ですので、
(今回は作品の表紙に合わないことがあっても)作風の気に入ったデザイナー様には
個人的にお話を相談させていただく場合もあると思っております。
その際には何卒よろしくお願い申し上げます。この度はまことにありがとうございました。
この度はご応募まことにありがとうございました。厳選なる選挙の結果、1名の作家さんが選ばれました。
選ばれました方には個別にお伝えいたしております。この度はまことにご応募ありがとうございました。

作家メンバーによる総選挙にて決定させて頂きました。皆様に広く愛される作品で、投票数も多く選ばせて頂きました。誠にありがとうございました。

今回、誠にご提案ありがとうございました。私自身は作家活動を継続していくつもりですので、また、個別にご依頼させて頂くこともあるかと思います。その時はよろしくお願いします。この度はありがとうございました。

```html
<!DOCTYPE html>
<html lang="ja">
<head>
<meta charset="utf-8">
<title>週末ごとに和みを探す読者へ贈る癒やしの四季手帳</title>
<link rel="stylesheet" href="https://fonts.googleapis.com/css2?family=M+PLUS+Rounded+1c:wght@500;700;800&display=swap">
<style>
  :root {
    --red-light: #d9262b;
    --red-main: #c0141b;
    --red-deep: #7d0a0e;
    --white: #ffffff;
    --ink: #1d1d1d;
    --sun: #f5b400;
    --sun-deep: #e07b00;
  }
  html, body {
    margin: 0;
    padding: 0;
    width: 750px;
    height: 1200px;
    overflow: hidden;
  }
  .cover {
    position: relative;
    width: 750px;
    height: 1200px;
    overflow: hidden;
    background: radial-gradient(ellipse at 50% 30%, var(--red-light) 0%, var(--red-main) 45%, var(--red-deep) 100%);
    font-family: "M PLUS Rounded 1c", sans-serif;
    color: var(--white);
  }
  .lead-arc {
    position: absolute;
    left: 0;
    top: 30px;
    width: 750px;
    height: 160px;
  }
  .lead-arc text {
    fill: var(--white);
    font-family: "M PLUS Rounded 1c", sans-serif;
    font-weight: 700;
    font-size: 38px;
  }
  .title {
    position: absolute;
    left: 0;
    width: 750px;
    text-align: center;
    margin: 0;
    font-weight: 800;
    line-height: 1;
    letter-spacing: 0.02em;
    text-shadow: 0 6px 14px rgba(80, 0, 0, 0.35);
  }
  .title-line { position: absolute; left: 0; width: 750px; text-align: center; }
  .title-line--1 { top: 190px; font-size: 108px; }
  .title-line--2 { top: 318px; font-size: 108px; }
  .title-line--3 { top: 448px; font-size: 92px; }
  .sparkle {
    position: absolute;
    width: 44px;
    height: 44px;
  }
  .sparkle line { stroke: var(--white); stroke-width: 4; stroke-linecap: round; }
  .sparkle--top { left: 618px; top: 60px; }
  .sparkle--side { left: 38px; top: 430px; }
  .author {
    position: absolute;
    left: 0;
    top: 580px;
    width: 750px;
    text-align: center;
    font-weight: 700;
    font-size: 40px;
    letter-spacing: 0.02em;
  }
  .author-mark { font-size: 32px; margin-left: 4px; }
  .crowd {
    position: absolute;
    left: 0;
    top: 640px;
    width: 750px;
    height: 560px;
    background:
      radial-gradient(circle at 20% 60%, rgba(245, 180, 0, 0.9) 0%, rgba(245, 180, 0, 0) 38%),
      radial-gradient(circle at 75% 45%, rgba(245, 180, 0, 0.85) 0%, rgba(245, 180, 0, 0) 35%),
      radial-gradient(circle at 50% 90%, rgba(224, 123, 0, 0.9) 0%, rgba(224, 123, 0, 0) 45%),
      linear-gradient(180deg, rgba(192, 20, 27, 0) 0%, rgba(224, 123, 0, 0.55) 40%, rgba(245, 180, 0, 0.75) 100%);
  }
  .bubble {
    position: absolute;
    background: var(--white);
    color: var(--ink);
    border-radius: 50%;
    display: flex;
    align-items: center;
    justify-content: center;
    text-align: center;
    font-weight: 700;
    font-size: 29px;
    line-height: 1.3;
    box-shadow: 0 4px 10px rgba(0, 0, 0, 0.2);
  }
  .bubble::after {
    content: "";
    position: absolute;
    width: 0;
    height: 0;
    border: 16px solid transparent;
  }
  .bubble--world { left: 80px; top: 800px; width: 200px; height: 140px; }
  .bubble--world::after { bottom: -22px; right: 40px; border-top: 22px solid var(--white); border-bottom: 0; transform: rotate(-20deg); }
  .bubble--life { left: 530px; top: 665px; width: 200px; height: 150px; }
  .bubble--life::after { bottom: -22px; left: 40px; border-top: 22px solid var(--white); border-bottom: 0; transform: rotate(20deg); }
  .bubble--saved { left: 395px; top: 960px; width: 230px; height: 145px; }
  .bubble--saved::after { top: -22px; left: 50px; border-bottom: 22px solid var(--white); border-top: 0; transform: rotate(-15deg); }
</style>
</head>
<body>
<main class="cover">
  <svg class="lead-arc" viewBox="0 0 750 160" aria-hidden="false">
    <defs>
      <path id="lead-curve" d="M 90 140 Q 375 40 660 140"/>
    </defs>
    <text text-anchor="middle"><textPath href="#lead-curve" startOffset="50%">週末ごとに和みを探す読者へ贈る</textPath></text>
  </svg>

  <svg class="sparkle sparkle--top" viewBox="0 0 44 44" aria-hidden="true">
    <line x1="22" y1="4" x2="22" y2="40"/><line x1="4" y1="22" x2="40" y2="22"/>
    <line x1="8" y1="8" x2="14" y2="14"/>
  </svg>
  <svg class="sparkle sparkle--side" viewBox="0 0 44 44" aria-hidden="true">
    <line x1="22" y1="4" x2="22" y2="40"/><line x1="4" y1="22" x2="40" y2="22"/>
    <line x1="36" y1="36" x2="30" y2="30"/>
  </svg>

  <h1 class="title">
    <span class="title-line title-line--1">癒やしの</span>
    <span class="title-line title-line--2">四季手帳</span>
    <span class="title-line title-line--3">ウィークリー</span>
  </h1>

  <p class="author" style="margin:0;">kanoe<span class="author-mark"> 著</span></p>

  <div class="crowd" role="img" aria-label="笑顔の黄色いボールがたくさん積み重なったイラスト"></div>

  <p class="bubble bubble--world" style="margin:0;">猫の昼寝は<br>街を照らす</p>
  <p class="bubble bubble--life" style="margin:0;">猫の昼寝は<br>毎日を照らす</p>
  <p class="bubble bubble--saved" style="margin:0;">私は猫の昼寝に<br>癒された</p>
</main>
</body>
</html>
```